Home Builder and Trade Supplier needs a Ad/leaflet/mail drop off leaflet design

HavenCrest is a business that builds homes, renovations, property maintenance and anything else construction related to residential homes. See photos I have attached that have a description of the business.

I'm after a double sided flyer for mail box drop offs. The market audience is up market expensive homes and offices. I have attached some examples of what i think would look good - I would like to see an example like or similar to that but by all means the designs you submit don't have to be a copy or similar. If you have something completely different in mind that you think would suit, please submit or even a rough draft if youre not sure I'll like it and you don't want to risk wasting time.

Please include the text and information in your designs that I have included in my examples.

Submissions before the 10 days are welcome and encouraged :)

Any questions, please feel free to ask on here or through email on: joram.k@mailvista.net

Pamphlet Size: 210 x 142mm (a quarter of an A4)
Double Sided Colour

Property Maintenance

Requirements
Must have
• Contact Us: 0412 958 601
www.havencresthomes.com.au
Double sided
Colour
Size: quater of an A4

```html
<!DOCTYPE html>
<html lang="en">
<head>
<meta charset="utf-8">
<title>HavenCrest Leaflet</title>
<link rel="stylesheet" href="https://fonts.googleapis.com/css2?family=Tinos:wght@400;700&family=Open+Sans:wght@400;600&family=Nothing+You+Could+Do&display=swap">
<style>
  :root {
    --orange: #f15a24;
    --grey: #a7a9ac;
    --ink: #111111;
    --paper: #ffffff;
    --tile-border: #6d6e71;
  }
  * { margin: 0; padding: 0; box-sizing: border-box; }
  html, body { width: 811px; height: 1200px; overflow: hidden; background: var(--paper); }
  .leaflet { position: relative; width: 811px; height: 1200px; background: var(--paper); font-family: "Tinos", "Times New Roman", serif; color: var(--ink); }

  .brand { position: absolute; left: 42px; top: 74px; display: flex; align-items: center; gap: 18px; }
  .brand-square { width: 72px; height: 72px; background: var(--grey); }
  .brand-name { font-family: "Open Sans", sans-serif; font-weight: 400; font-size: 62px; letter-spacing: 1px; color: var(--orange); line-height: 1; }

  .contact-callout { position: absolute; left: 452px; top: 52px; font-family: "Nothing You Could Do", cursive; font-size: 44px; color: var(--orange); transform: rotate(-12deg); transform-origin: left bottom; white-space: nowrap; }
  .contact-phone { position: absolute; left: 543px; top: 116px; font-size: 37px; color: var(--grey); letter-spacing: 0.5px; }

  .intro { position: absolute; left: 40px; top: 220px; width: 735px; font-size: 18px; line-height: 29px; }
  .intro p + p { margin-top: 20px; }

  .service-grid { position: absolute; left: 82px; top: 354px; display: grid; grid-template-columns: repeat(5, 98px); column-gap: 31px; row-gap: 49px; }
  .service-grid .tile:nth-child(5n) { margin-left: 18px; }
  .tile { width: 98px; height: 98px; border: 2px solid var(--tile-border); border-radius: 13px; box-shadow: 1px 2px 3px rgba(0,0,0,0.35); }
  .t1 { background: linear-gradient(135deg, #e6e3dc, #b9b4aa); }
  .t2 { background: linear-gradient(135deg, #f6c21a, #d79b0a 60%, #e9e6de); }
  .t3 { background: linear-gradient(160deg, #f1efe9, #8a6a44); }
  .t4 { background: linear-gradient(135deg, #f2f4f8, #3f6fc4 70%, #e8ecf4); }
  .t5 { background: linear-gradient(135deg, #f0ece6, #c24a3a 50%, #e6e2d8); }
  .t6 { background: linear-gradient(135deg, #e43a2f, #f2b21c 35%, #2f8fd0 70%, #5a9a3a); }
  .t7 { background: linear-gradient(135deg, #77787b, #4d4e50); }
  .t8 { background: linear-gradient(160deg, #f5f5f3, #7aa25a 60%, #3c8d3a); }
  .t9 { background: linear-gradient(170deg, #ffffff 30%, #a9442b 60%, #7a2e1d); }
  .t10 { background: linear-gradient(180deg, #d9d9d7, #8a8b8a 55%, #5f8a3c); }
  .t11 { background: linear-gradient(160deg, #8fc3ea, #1f5da6 55%, #3a7a3a); }
  .t12 { background: linear-gradient(135deg, #ffffff, #f0b020 40%, #e4417a 65%, #2aa0d8); }
  .t13 { background: linear-gradient(160deg, #ffffff, #9a8a78 55%, #5d4d40); }
  .t14 { background: linear-gradient(135deg, #ffffff 20%, #6e6f70 50%, #4a4b4c); }
  .t15 { background: linear-gradient(135deg, #dfe8ee, #8fa6b4 60%, #c9d3d8); }
  .t16 { background: linear-gradient(160deg, #cfe0ee, #f4f4f2 50%, #9aa3a8); }
  .t17 { background: linear-gradient(180deg, #9b5a3a, #6b3a24 70%, #c9c7c2); }
  .t18 { background: linear-gradient(135deg, #ffffff, #d39a52 50%, #b5773a); }
  .t19 { background: linear-gradient(160deg, #3b3d42, #c9a23a 55%, #2c2d30); }
  .t20 { background: linear-gradient(135deg, #ffffff, #b9c0c6 50%, #c0392b 85%); }

  .services { position: absolute; left: 42px; top: 912px; }
  .services-heading { font-size: 20px; font-weight: 700; margin-left: 4px; }
  .services-list { position: absolute; top: 32px; left: 0; width: 740px; height: 120px; list-style: none; }
  .services-list li { position: absolute; font-size: 18px; white-space: nowrap; }
  .services-list li::before { content: "\2022"; margin-right: 5px; }

  .footer-band { position: absolute; left: 0; top: 1058px; width: 811px; height: 142px; background: var(--orange); display: flex; align-items: center; justify-content: center; }
  .footer-url { font-family: "Open Sans", sans-serif; font-size: 27px; color: var(--paper); letter-spacing: 0.5px; }
</style>
</head>
<body>
<main class="leaflet">
  <header class="brand">
    <span class="brand-square"></span>
    <span class="brand-name">HavenCrest</span>
  </header>
  <div class="contact-callout">Contact us!</div>
  <div class="contact-phone">0412 958 601</div>

  <section class="intro">
    <p>HavenCrest is one of the preferred home builders and &nbsp;residential trade supplier for customers across Sydney.A one stop shop, we can build your entire home or supply you with our specialist tradesmen.</p>
    <p>No matter how small or large your job is, contact us to find out how we can help you.</p>
  </section>

  <section class="service-grid">
    <div class="tile t1" role="img" aria-label="Architectural drawing with compass"></div>
    <div class="tile t2" role="img" aria-label="Yellow hard hat on plans"></div>
    <div class="tile t3" role="img" aria-label="Tool belt with tools"></div>
    <div class="tile t4" role="img" aria-label="Blue engineering model"></div>
    <div class="tile t5" role="img" aria-label="Electrical wires on a plan"></div>
    <div class="tile t6" role="img" aria-label="Paint colour swatches"></div>
    <div class="tile t7" role="img" aria-label="Grey floor tiles"></div>
    <div class="tile t8" role="img" aria-label="Garden tools and hose"></div>
    <div class="tile t9" role="img" aria-label="Bricklaying with trowel"></div>
    <div class="tile t10" role="img" aria-label="Garage door and driveway"></div>
    <div class="tile t11" role="img" aria-label="Glass office tower"></div>
    <div class="tile t12" role="img" aria-label="Shopping bags in hand"></div>
    <div class="tile t13" role="img" aria-label="Excavator bucket"></div>
    <div class="tile t14" role="img" aria-label="Roof shingles"></div>
    <div class="tile t15" role="img" aria-label="Glazed building facade"></div>
    <div class="tile t16" role="img" aria-label="Curved modern building"></div>
    <div class="tile t17" role="img" aria-label="Timber slat fence"></div>
    <div class="tile t18" role="img" aria-label="Timber plank and tape measure"></div>
    <div class="tile t19" role="img" aria-label="Retail showroom interior"></div>
    <div class="tile t20" role="img" aria-label="Plumbing tools and fittings"></div>
  </section>

  <section class="services">
    <h2 class="services-heading">Contact Us for:</h2>
    <ul class="services-list">
      <li style="left:0;top:0">New Homes</li>
      <li style="left:0;top:29px">Renovations</li>
      <li style="left:0;top:57px">Architecture</li>
      <li style="left:0;top:85px">Engineering</li>
      <li style="left:142px;top:0">Maintenance</li>
      <li style="left:142px;top:29px">Strata</li>
      <li style="left:142px;top:57px">Air Conditioning</li>
      <li style="left:142px;top:85px">Plumbing</li>
      <li style="left:307px;top:0">Painting</li>
      <li style="left:307px;top:29px">Electrical</li>
      <li style="left:307px;top:57px">Lawn Mowing</li>
      <li style="left:307px;top:85px">Landscaping</li>
      <li style="left:474px;top:0">Tiling</li>
      <li style="left:474px;top:29px">Glazing</li>
      <li style="left:474px;top:57px">Bricklaying</li>
      <li style="left:474px;top:85px">Roofing</li>
      <li style="left:634px;top:0">Demolition</li>
      <li style="left:634px;top:29px">Excavation</li>
      <li style="left:634px;top:57px">Carpentry</li>
      <li style="left:634px;top:85px">Cleaning</li>
    </ul>
  </section>

  <footer class="footer-band">
    <span class="footer-url">www.havencresthomes.com.au</span>
  </footer>
</main>
</body>
</html>
```